Need a Back Drop Design for Trade Show

10x10 back drop
Economy Retractable Banner Stand with Full Color Standard Graphic
• 33.5"w x 80"h
8.25' Feather Flag with Spike Base and X-Base
6' x 3' Vinyl Banner, Heavy Duty

Will need one for Alarm company
Will need one for Solar company
Would like them to look modern and branded
I've added links of our websites as well as all our logos. We are looking for a clean sharp modern look thats also bold. I've attached all our old marketing material. Im looking for something different thats not the same.

ferntidesolar.example
getferntide.example

Target Market(s)

Home Owners

Industry/Entity Type

Smart Security Systems & Solar Systems

Font styles to use
Sans Serif

Colors
0054AA
0677BA
7BADD7
CADEEF
E8F1F8

Requirements
Must have
• Our Logo and company colors

```html
<!DOCTYPE html>
<html lang="en">
<head>
<meta charset="utf-8">
<title>Ferntide Smart Security – Trade Show Backdrop</title>
<link rel="stylesheet" href="https://fonts.googleapis.com/css2?family=Montserrat:wght@400;600;700;800&display=swap">
<style>
  :root {
    --brand-deep: #0054AA;
    --brand-blue: #0677BA;
    --brand-sky: #7BADD7;
    --brand-mist: #CADEEF;
    --brand-ice: #E8F1F8;
    --headline: #1167b1;
    --bg-top: #9db9e0;
    --bg-glow: #f4f6fb;
    --bg-bottom: #7a80b0;
    --white: #ffffff;
  }
  html, body {
    margin: 0;
    padding: 0;
    width: 1200px;
    height: 1200px;
    overflow: hidden;
  }
  .backdrop {
    position: relative;
    width: 1200px;
    height: 1200px;
    overflow: hidden;
    font-family: "Montserrat", sans-serif;
    background:
      radial-gradient(ellipse 620px 300px at 330px 560px, var(--bg-glow) 0%, rgba(244,246,251,0.6) 45%, rgba(244,246,251,0) 100%),
      linear-gradient(180deg, var(--bg-top) 0%, #b7c9e8 35%, #aab4da 60%, var(--bg-bottom) 100%);
  }
  .backdrop svg { display: block; }
  .brand-name { font-weight: 700; fill: var(--white); }
  .brand-tagline { font-weight: 400; fill: var(--white); letter-spacing: 1px; }
  .headline { font-weight: 800; fill: var(--headline); }
  .service-label {
    font-weight: 700;
    font-size: 15px;
    fill: var(--white);
    letter-spacing: 0.3px;
  }
  .service-band { fill: var(--brand-blue); }
  .service-frame { fill: none; stroke: var(--white); stroke-width: 4; }
  .service-icon-disc { fill: var(--white); fill-opacity: 0.85; }
  .service-icon { fill: none; stroke: var(--brand-blue); stroke-width: 5; stroke-linecap: round; stroke-linejoin: round; }
  .service-icon-fill { fill: var(--brand-blue); }
  .footer-bar { fill: var(--brand-blue); }
</style>
</head>
<body>
<main class="backdrop">
  <svg width="1200" height="1200" viewBox="0 0 1200 1200" xmlns="http://www.w3.org/2000/svg">
    <defs>
      <linearGradient id="camera-tone" x1="0" y1="0" x2="1" y2="1">
        <stop offset="0" stop-color="#c9d6f0"/>
        <stop offset="0.6" stop-color="#8f9fd6"/>
        <stop offset="1" stop-color="#6f78b8"/>
      </linearGradient>
      <radialGradient id="camera-glow" cx="0.45" cy="0.85" r="0.6">
        <stop offset="0" stop-color="#e9a2c8" stop-opacity="0.7"/>
        <stop offset="1" stop-color="#8f9fd6" stop-opacity="0"/>
      </radialGradient>
      <linearGradient id="install-tone" x1="0" y1="0" x2="1" y2="1">
        <stop offset="0" stop-color="#f4f4f5"/>
        <stop offset="0.55" stop-color="#dcd3cc"/>
        <stop offset="1" stop-color="#9a6a4c"/>
      </linearGradient>
      <linearGradient id="phone-tone" x1="0" y1="0" x2="1" y2="1">
        <stop offset="0" stop-color="#e4e9ef"/>
        <stop offset="0.5" stop-color="#5d7aa5"/>
        <stop offset="1" stop-color="#1f3554"/>
      </linearGradient>
      <linearGradient id="panel-tone" x1="0" y1="0" x2="1" y2="1">
        <stop offset="0" stop-color="#c9cacd"/>
        <stop offset="0.5" stop-color="#f2f2f2"/>
        <stop offset="1" stop-color="#b99880"/>
      </linearGradient>
      <linearGradient id="support-tone" x1="0" y1="0" x2="1" y2="1">
        <stop offset="0" stop-color="#e9ecef"/>
        <stop offset="0.5" stop-color="#d8cfc6"/>
        <stop offset="1" stop-color="#c7ccd3"/>
      </linearGradient>
    </defs>

    <!-- Camera visual, top right -->
    <g class="hero-visual" role="img" aria-label="Photo of a white dome security camera mounted on a ceiling">
      <path d="M745 0 H1200 V415 Q1000 430 850 360 Q760 300 745 150 Z" fill="url(#camera-tone)"/>
      <path d="M745 0 H1200 V415 Q1000 430 850 360 Q760 300 745 150 Z" fill="url(#camera-glow)"/>
    </g>

    <!-- Brand lockup -->
    <g class="brand-lockup">
      <rect x="62" y="86" width="96" height="96" fill="var(--white)"/>
      <text class="brand-name" x="200" y="173" font-size="82">Ferntide</text>
      <text class="brand-tagline" x="588" y="212" font-size="29" text-anchor="end">SMART SECURITY</text>
    </g>

    <!-- Headline -->
    <g class="headline-group">
      <text class="headline" x="60" y="445" font-size="148" textLength="680" lengthAdjust="spacingAndGlyphs">A POWER</text>
      <text class="headline" x="62" y="538" font-size="100" textLength="840" lengthAdjust="spacingAndGlyphs">THAT GUARDS YOU</text>
    </g>

    <!-- Service panels -->
    <g class="services">
      <g class="service">
        <polygon role="img" aria-label="Photo of a technician installing a bullet security camera" points="60,617 312,617 380,848 128,848" fill="url(#install-tone)"/>
        <polygon class="service-frame" points="60,617 312,617 380,848 128,848"/>
        <circle class="service-icon-disc" cx="220" cy="732" r="36"/>
        <path class="service-icon" d="M204 733 L215 745 L237 720"/>
        <polygon class="service-band" points="128,848 380,848 394,896 142,896"/>
        <text class="service-label" x="258" y="869" text-anchor="middle">PROFESSIONAL</text>
        <text class="service-label" x="260" y="886" text-anchor="middle">INSTALLATION</text>
      </g>
      <g class="service">
        <polygon role="img" aria-label="Photo of a hand holding a smartphone running a smart home app" points="316,617 564,617 632,848 384,848" fill="url(#phone-tone)"/>
        <polygon class="service-frame" points="316,617 564,617 632,848 384,848"/>
        <circle class="service-icon-disc" cx="472" cy="732" r="36"/>
        <rect class="service-icon" x="460" y="712" width="24" height="40" rx="4"/>
        <circle class="service-icon-fill" cx="472" cy="745" r="2.5"/>
        <polygon class="service-band" points="384,848 632,848 646,896 398,896"/>
        <text class="service-label" x="510" y="869" text-anchor="middle">100% CELLULAR</text>
        <text class="service-label" x="512" y="886" text-anchor="middle">COMMUNICATION</text>
      </g>
      <g class="service">
        <polygon role="img" aria-label="Photo of a finger pressing keys on a wall alarm keypad" points="568,617 816,617 884,848 636,848" fill="url(#panel-tone)"/>
        <polygon class="service-frame" points="568,617 816,617 884,848 636,848"/>
        <circle class="service-icon-disc" cx="724" cy="732" r="36"/>
        <g class="service-icon-fill">
          <circle cx="712" cy="716" r="3.5"/><circle cx="724" cy="716" r="3.5"/><circle cx="736" cy="716" r="3.5"/>
          <circle cx="712" cy="727" r="3.5"/><circle cx="724" cy="727" r="3.5"/><circle cx="736" cy="727" r="3.5"/>
          <circle cx="712" cy="738" r="3.5"/><circle cx="724" cy="738" r="3.5"/><circle cx="736" cy="738" r="3.5"/>
          <circle cx="724" cy="749" r="3.5"/>
        </g>
        <polygon class="service-band" points="636,848 884,848 898,896 650,896"/>
        <text class="service-label" x="762" y="869" text-anchor="middle">COMMERCIAL</text>
        <text class="service-label" x="764" y="886" text-anchor="middle">ALARM SYSTEMS</text>
      </g>
      <g class="service">
        <polygon role="img" aria-label="Photo of a smiling monitoring centre operator wearing a headset" points="820,617 1068,617 1136,848 888,848" fill="url(#support-tone)"/>
        <polygon class="service-frame" points="820,617 1068,617 1136,848 888,848"/>
        <circle class="service-icon-disc" cx="976" cy="732" r="36"/>
        <circle class="service-icon" cx="976" cy="732" r="20"/>
        <path class="service-icon" d="M976 720 V733 L986 739"/>
        <polygon class="service-band" points="888,848 1136,848 1150,896 902,896"/>
        <text class="service-label" x="1014" y="869" text-anchor="middle">24/7 LIVE</text>
        <text class="service-label" x="1016" y="886" text-anchor="middle">MONITORING</text>
      </g>
    </g>

    <!-- Footer band -->
    <rect class="footer-bar" x="0" y="1121" width="1200" height="79"/>
  </svg>
</main>
</body>
</html>
```